Used Semi Truck Website Redesign

We are redoing the website backend and would like to also do a front end redesign. I would like a Mobile and Desktop mockup for each page. The website has more mobile visitors than desktop visitors. Our competitor is http://www.haulmarketbay.example. We don't want to copy them exactly but we want a site that looks more like that. We need the functionality of that site. One big difference is that we also sell parts and trailers.

We need a redesign for front page, product detail page, search result page, content page. It is very important that the site is very easy to use on mobile devices. Our target audience is Truck drivers.

Feel free to use demo fonts stock images, and icons. We will purchase necessary 3rd party media when a winner is chosen.

Target Market(s)

People who want to buy used trucks.

Coding

Coded - Design and coding required

Number of Pages Required

5+ page

Requirements
Must have
• Mockup for Desktop and Mobile pages.

```html
<!DOCTYPE html>
<html lang="en">
<head>
<meta charset="utf-8">
<title>Terms &amp; Conditions – HaulYard</title>
<link href="https://fonts.googleapis.com/css2?family=Roboto:wght@300;400;500&display=swap" rel="stylesheet">
<style>
:root{
  --ink:#1b1c23;
  --text:#333640;
  --muted:#8a8d96;
  --accent:#f0191f;
  --panel:#efeff3;
  --white:#ffffff;
  --footer-text:#c9cad0;
}
*{margin:0;padding:0;box-sizing:border-box}
html,body{width:1138px;height:1200px;overflow:hidden}
body{font-family:'Roboto',sans-serif;background:var(--white);color:var(--text);position:relative}
a{color:inherit;text-decoration:none}

.topbar{position:absolute;left:0;top:0;width:1138px;height:49px;background:var(--ink);z-index:2}
.brand{position:absolute;left:84px;top:14px;font-size:17px;font-weight:400;color:var(--white);letter-spacing:.3px}
.mainnav{position:absolute;left:421px;top:0;display:flex;align-items:center;height:49px;font-size:12px;color:#b9bac2}
.mainnav a{margin-right:24px;position:relative}
.mainnav a.active{color:var(--white)}
.mainnav a.active::before{content:"";position:absolute;left:0;right:0;top:-18px;height:2px;background:var(--white)}
.mainnav .sep{width:1px;height:16px;background:#4a4b55;margin:0 18px 0 -6px}
.social{position:absolute;right:84px;top:17px;display:flex;gap:19px}
.social span{width:12px;height:12px;border-radius:50%;background:var(--white);display:block}

.hero{position:absolute;left:0;top:49px;width:1138px;height:187px;background:linear-gradient(100deg,#2b2d38 0%,#3d404d 35%,#4a4c58 55%,#3a3438 80%,#2c2e38 100%)}
.hero-title{position:absolute;left:0;right:0;top:55px;text-align:center;color:var(--white);font-size:20px;font-weight:300}
.hero-actions{position:absolute;left:458px;top:93px;display:flex;gap:6px}
.hero-actions a{width:71px;height:37px;background:rgba(255,255,255,.18);color:var(--white);font-size:12px;display:flex;align-items:center;justify-content:center}

.subnav{position:absolute;left:0;top:236px;width:1138px;height:51px;background:var(--panel);border-bottom:1px solid #e2e2e8}
.subnav a{position:absolute;top:19px;font-size:12px;color:var(--ink)}
.subnav a.current{left:191px;color:var(--muted)}
.subnav a.current::after{content:"";position:absolute;left:0;width:74px;top:31px;height:2px;background:var(--accent)}
.subnav a.next{left:294px}

.content{position:absolute;left:191px;top:324px;width:755px}
.section-title{font-size:20px;font-weight:400;color:var(--ink);position:relative;padding-bottom:14px}
.section-title::after{content:"";position:absolute;left:0;bottom:0;width:38px;height:1px;background:#c9c9cf}
.content p{font-size:12.6px;line-height:21px;margin-top:20px}
.callout{margin-top:24px;background:var(--panel);padding:36px 38px 40px}
.callout h3{font-size:15px;font-weight:500;color:var(--ink);text-transform:uppercase}
.callout p{margin-top:11px}
.privacy{margin-top:30px}

.to-top{position:absolute;left:1077px;top:874px;width:38px;height:38px;border-radius:50%;background:var(--accent);z-index:3;display:flex;align-items:center;justify-content:center}

.footer{position:absolute;left:0;top:894px;width:1138px;height:263px;background:var(--ink);color:var(--footer-text)}
.fcol{position:absolute;top:52px}
.fcol h4{font-size:15px;font-weight:500;color:var(--white);position:relative;padding-bottom:10px}
.fcol h4::after{content:"";position:absolute;left:0;bottom:0;width:29px;height:1px;background:#6b6c75}
.feed{width:290px;margin-top:15px}
.feed-item{font-size:11px;line-height:18.5px;position:relative;padding-left:14px}
.feed-item + .feed-item{margin-top:10px;padding-top:10px;border-top:1px solid #34353e}
.feed-item .mark{position:absolute;left:0;top:6px;width:7px;height:7px}
.feed-item + .feed-item .mark{top:16px}
.feed-item .meta{display:flex;align-items:center;gap:5px;color:var(--white);font-weight:500;margin-top:2px;margin-left:-1px}
.col-blogs{left:84px}
.col-updates{left:444px}
.col-links{left:800px}
.links{display:grid;grid-template-columns:126px 130px;row-gap:9px;margin-top:15px;font-size:11px}
.links a::before{content:"›";margin-right:5px;color:var(--muted)}

.legal{position:absolute;left:0;top:1157px;width:1138px;height:43px;background:var(--accent);color:var(--white);font-size:11px;font-weight:500}
.legal .copy{position:absolute;left:84px;top:15px}
.legal nav{position:absolute;right:84px;top:15px;display:flex;gap:27px}
</style>
</head>
<body>

<header class="topbar">
  <a class="brand" href="#">HaulYard</a>
  <nav class="mainnav">
    <a class="active" href="#">Login</a>
    <a href="#">Register</a>
    <span class="sep"></span>
    <a href="#">Find a dealer</a>
    <a href="#">Dealer Login</a>
  </nav>
  <div class="social" aria-label="Social links">
    <span></span><span></span><span></span><span></span><span></span>
  </div>
</header>

<section class="hero" role="img" aria-label="Dim photo of a truck and freight rail yard">
  <h1 class="hero-title">Terms &amp; Conditions</h1>
  <div class="hero-actions">
    <a href="#">Find</a><a href="#">Sell</a><a href="#">Research</a>
  </div>
</section>

<nav class="subnav">
  <a class="current" href="#">Privacy Policy</a>
  <a class="next" href="#">Terms &amp; Conditions</a>
</nav>

<main class="content">
  <h2 class="section-title">Basic Policy</h2>
  <p>Donec pede justo fringilla vel aliquet nec vulputate eget arcu in enim justo rhoncus ut imperdiet a venenatis vitae, justo nullam dictum felis eu pede mollis pretium integer tincidunt cras dapibus vivamus elementum semper nisi aenean vulputate eleifend tellus aenean leo ligula porttitor eu consequat vitae eleifend ac enim. Aliquam lorem ante dapibus in viverra quis feugiat a tellus phasellus viverra nulla ut metus varius laoreet quisque rutrum.</p>

  <div class="callout">
    <h3>Some heading here</h3>
    <p>Pede justo fringilla vel aliquet nec vulputate eget arcu in enim justo rhoncus ut imperdiet a venenatis vitae, justo nullam dictum felis eu pede mollis pretium integer tincidunt cras dapibus vivamus elementum semper nisi aenean vulputate eleifend tellus aenean leo ligula porttitor eu consequat vitae eleifend ac enim. aliquam lorem ante dapibus in viverra quis feugiat a tellus phasellus&nbsp; laoreet quisque rutrum viverra nulla ut metus varius.</p>
  </div>

  <h2 class="section-title privacy">Privacy</h2>
  <p>Fringilla vel aliquet nec vulputate eget arcu in enim justo rhoncus ut imperdiet a venenatis vitae, justo nullam dictum felis eu pede mollis pretium integer tincidunt cras dapibus vivamus elementum semper nisi aenean vulputate eleifend tellus aenean leo ligula porttitor eu consequat vitae eleifend ac enim. Aliquam lorem ante dapibus in viverra quis feugiat a tellus phasellus viverra nulla ut metus varius laoreet quisque dec norem.</p>
</main>

<a class="to-top" href="#" aria-label="Back to top">
  <svg width="10" height="12" viewBox="0 0 10 12"><path d="M5 11V1M1.5 4.5 5 1l3.5 3.5" fill="none" stroke="#fff" stroke-width="1.2"/></svg>
</a>

<footer class="footer">
  <div class="fcol col-blogs">
    <h4>Our Blogs</h4>
    <div class="feed">
      <div class="feed-item">
        <svg class="mark" viewBox="0 0 8 8"><circle cx="1.2" cy="6.8" r="1.2" fill="#fff"/><path d="M0 3.5A4.5 4.5 0 0 1 4.5 8M0 .5A7.5 7.5 0 0 1 7.5 8" fill="none" stroke="#fff" stroke-width="1.1"/></svg>
        Dictum nullam felis eu pede mollis pretium integer tinci-dunt cras dapibus vivamus elementum semper.
        <div class="meta">10-Dec-2016</div>
      </div>
      <div class="feed-item">
        <svg class="mark" viewBox="0 0 8 8"><circle cx="1.2" cy="6.8" r="1.2" fill="#fff"/><path d="M0 3.5A4.5 4.5 0 0 1 4.5 8M0 .5A7.5 7.5 0 0 1 7.5 8" fill="none" stroke="#fff" stroke-width="1.1"/></svg>
        Dec dictum felis eu pede mollis pretium integer tincidunt cras dapibus vivamus elementum semper dipsum.
        <div class="meta">10-Dec-2016</div>
      </div>
    </div>
  </div>

  <div class="fcol col-updates">
    <h4>Latest Updates</h4>
    <div class="feed">
      <div class="feed-item">
        <svg class="mark" viewBox="0 0 8 8"><circle cx="4" cy="4" r="3.5" fill="#fff"/></svg>
        Nullam dictum felis eu pede mollis pretium integer tinci-dunt cras dapibus vivamus elementum semper.
        <div class="meta"><svg width="11" height="9" viewBox="0 0 11 9"><path d="M1 8V5.5h8M6.5 3 9 5.5 6.5 8" fill="none" stroke="#fff" stroke-width="1.2"/></svg>Share</div>
      </div>
      <div class="feed-item">
        <svg class="mark" viewBox="0 0 8 8"><circle cx="4" cy="4" r="3.5" fill="#fff"/></svg>
        Lorem dictum felis eu pede mollis pretium integer tinci-dunt cras dapibus vivamus elementum sem ipsum.
        <div class="meta"><svg width="11" height="9" viewBox="0 0 11 9"><path d="M1 8V5.5h8M6.5 3 9 5.5 6.5 8" fill="none" stroke="#fff" stroke-width="1.2"/></svg>Share</div>
      </div>
    </div>
  </div>

  <div class="fcol col-links">
    <h4>Resource Advertisers</h4>
    <nav class="links">
      <a href="#">Insurance</a><a href="#">Truck Parts</a>
      <a href="#">Jobs &amp; Training</a><a href="#">Steel Buildings</a>
      <a href="#">Vehicle History</a><a href="#">Fuel Management</a>
      <a href="#">Truck Bodies</a><a href="#">Shipping &amp; Transport</a>
      <a href="#">Finance/Lease</a><a href="#">View All</a>
    </nav>
  </div>
</footer>

<div class="legal">
  <span class="copy">© Company name here, All Rights Reserved.</span>
  <nav><a href="#">Trucks for sale</a><a href="#">New Arrivals</a><a href="#">Site map</a></nav>
</div>

</body>
</html>
```